Logo & Visitenkarte für Coach
Zielgruppe
Was:
Sie haben eine Idee und wir coach Sie bei der Umsetzung.
Wer:
Alle Unternehmen oder Privatperson mit einer Idee.
Aufgabenstellung
Als Anhang sende ich Ihnen ein paar Bilder von einem Stein. Es geht mir nicht um die Farbgebung sondern nur um die 4 Flächen dieses Steines.
Meine Firma berut auf drei Säulen, der Stein hat eine Grundfläche lila und drei Flächen in pink, Wissen, Liebe und Glaube.

```html
<!DOCTYPE html>
<html lang="de">
<head>
<meta charset="utf-8">
<title>Zielwerkhaus – Visitenkarten</title>
<link rel="stylesheet" href="https://fonts.googleapis.com/css2?family=Open+Sans:wght@400;600;700&display=swap">
<style>
  :root {
    --green: #1fa23a;
    --charcoal: #3d3d3d;
    --grey-text: #4a4a4a;
    --paper: #ffffff;
    --bg-light: #f2f2f2;
    --bg-dark: #cfcfcf;
    --font: "Open Sans", Arial, sans-serif;
  }
  * { box-sizing: border-box; margin: 0; padding: 0; }
  html, body { width: 1200px; height: 675px; overflow: hidden; }
  body {
    font-family: var(--font);
    background: radial-gradient(ellipse at 60% 30%, var(--bg-light) 0%, #e4e4e4 55%, var(--bg-dark) 100%);
    position: relative;
  }
  .card {
    position: absolute;
    width: 520px;
    height: 336px;
    background: var(--paper);
    box-shadow: 0 12px 30px rgba(0,0,0,.18);
    overflow: hidden;
  }
  .card svg.card-shapes { position: absolute; inset: 0; width: 100%; height: 100%; }

  /* Rückseite */
  .card-back { left: 50px; top: 60px; }
  .back-brand {
    position: absolute; right: 36px; top: 30px;
    display: flex; align-items: center; gap: 8px;
    font-weight: 700; font-size: 15px; letter-spacing: .5px; color: var(--charcoal);
  }
  .brand-dot { width: 14px; height: 14px; border-radius: 50%; background: var(--green); }
  .back-address {
    position: absolute; right: 36px; top: 68px;
    font-style: normal;
    text-align: right; font-size: 12.5px; line-height: 1.55; color: var(--grey-text);
  }
  .back-address .gap { height: 10px; }
  .name-tag {
    position: absolute; left: 0; top: 212px;
    background: var(--green); color: #fff;
    font-weight: 700; font-size: 15px; letter-spacing: 1.5px; text-transform: uppercase;
    padding: 9px 26px 9px 24px; border-radius: 0 6px 6px 0;
  }
  .back-slogan {
    position: absolute; left: 0; right: 0; bottom: 0; height: 46px;
    background: var(--charcoal); color: #fff;
    font-size: 13px; letter-spacing: .3px;
    display: flex; align-items: center; justify-content: flex-end; padding-right: 36px;
  }

  /* Vorderseite */
  .card-front { left: 630px; top: 60px; }
  .front-brand {
    position: absolute; left: 0; right: 0; top: 138px;
    display: flex; align-items: center; justify-content: center; gap: 12px;
    font-weight: 700; font-size: 34px; letter-spacing: 1px; color: var(--charcoal);
  }
  .front-brand .brand-dot { width: 26px; height: 26px; }

  /* Logoblock */
  .logo-lockup {
    position: absolute; right: 70px; bottom: 70px;
    display: flex; align-items: center; gap: 12px;
    font-weight: 700; font-size: 26px; letter-spacing: 1px; color: var(--charcoal);
  }
  .logo-lockup .brand-dot { width: 22px; height: 22px; }
</style>
</head>
<body>

  <section class="card card-back" aria-label="Visitenkarte Rückseite">
    <svg class="card-shapes" viewBox="0 0 520 336" aria-hidden="true">
      <polygon points="520,190 520,196 320,290 309,290" fill="var(--charcoal)"/>
    </svg>
    <div class="back-brand"><span class="brand-dot"></span>ZIELWERKHAUS</div>
    <address class="back-address">
      Zielwerkhaus<br>
      Lindenweg 7<br>
      54321 Beispielfeld
      <div class="gap"></div>
      Tel.: 09876 / 54321<br>
      kontakt@zielwerkhaus-demo.de
    </address>
    <div class="name-tag">Lena Beispiel</div>
    <p class="back-slogan">Sie bringen die Idee. Wir zeigen Ihnen den Weg!</p>
  </section>

  <section class="card card-front" aria-label="Visitenkarte Vorderseite">
    <svg class="card-shapes" viewBox="0 0 520 336" aria-hidden="true">
      <polygon points="0,0 150,0 0,62" fill="var(--charcoal)"/>
      <path d="M170,336 C300,300 430,220 520,140 L520,165 C440,235 330,305 230,336 Z" fill="var(--green)"/>
    </svg>
    <div class="front-brand"><span class="brand-dot"></span>ZIELWERKHAUS</div>
  </section>

  <div class="logo-lockup"><span class="brand-dot"></span>ZIELWERKHAUS</div>

</body>
</html>
```